Logo/Business Print Card Design

We had two businesses and had two separate logos and business cards. These two businesses have become one which is now only called Verdant Wares. We need to incorporate the characteristics and designs into 1 final logo and design under Verdant Wares.

Our Business is about sourcing products to fill in gaps in the market majority in the Retail/Grocery Market – from developing the product to designing packaging, including warehousing, and marketing the final finished product.

The logo should communicate: 1) product being sourced 2) created and developed and 3) Introduced to market and managed.

Please find attached Word Document 1 - to see the current logo and business designs that need to be incorporated.

Target Market(s)

Retailers, Buyers, Agents, Suppliers – Business to Business customers and clients we deal with.

Industry/Entity Type

Business

Requirements
Must have
• Must Have:

• The logo should communicate: 1) Sourcing 2) Developing and 3) Introducing to the Market
• The current attached illustration (image 1) shows 3 squares, the first being sourcing the product, the second indicates developing the product ready to take it to the market and the third depicts the product on the shelf ready for end consumers.
• It should be a modernized version of attached image 1.
Nice to have
• Image 2 incorporated into design
• The colour concept – company preference is Orange and Green same as Market Bridge Logo.
Should not have
• Old style fonts and designs – should be clean and uncluttered

```html
<!DOCTYPE html>
<html lang="en">
<head>
<meta charset="utf-8">
<title>Verdant Wares – Logo and Business Card</title>
<link rel="stylesheet" href="https://fonts.googleapis.com/css2?family=Source+Sans+3:wght@400;600&display=swap">
<style>
  :root {
    --ink: #333335;
    --green: #8dc63f;
    --orange: #fbb040;
    --orange-soft: #fdb448;
    --white: #ffffff;
    --card-edge: #d6d6d6;
    --text-dark: #2b2b2b;
  }
  * { margin: 0; padding: 0; box-sizing: border-box; }
  html, body {
    width: 1200px;
    height: 901px;
    overflow: hidden;
    background: var(--white);
    font-family: "Source Sans 3", "Myriad Pro", Arial, sans-serif;
  }
  .sheet { position: relative; width: 1200px; height: 901px; }

  .wordmark {
    position: absolute;
    display: flex;
    align-items: flex-start;
    gap: 0.18em;
    font-weight: 600;
    line-height: 0.9;
    letter-spacing: -0.02em;
  }
  .wordmark__square {
    width: 0.22em;
    height: 0.22em;
    margin-top: 0.08em;
    background: currentColor;
    flex: none;
  }
  .wordmark__text { display: flex; flex-direction: column; align-items: flex-end; }
  .wordmark__tag { font-size: 0.42em; letter-spacing: 0; margin-top: 0.12em; }

  /* Master logo */
  .logo-master { left: 170px; top: 196px; font-size: 104px; color: var(--ink); }

  /* Front of card */
  .card-front {
    position: absolute;
    left: 15px; top: 424px;
    width: 728px; height: 416px;
    background: var(--green);
  }
  .card-front__band {
    position: absolute; left: 0; bottom: 0;
    width: 100%; height: 25px;
    background: var(--orange);
  }
  .logo-front { left: 195px; top: 160px; font-size: 78px; color: var(--white); }

  /* Back of card */
  .card-back {
    position: absolute;
    left: 779px; top: 113px;
    width: 398px; height: 730px;
    background: var(--white);
    border: 1px solid var(--card-edge);
  }
  .card-back__band {
    position: absolute; left: 0; top: 226px;
    width: 100%; height: 157px;
    background: var(--orange-soft);
  }
  .logo-back { left: 125px; top: 118px; font-size: 44px; color: var(--orange); }

  .contact {
    position: absolute;
    right: 20px; top: 436px;
    text-align: right;
    color: var(--text-dark);
    letter-spacing: 0.18em;
  }
  .contact__name { font-size: 21px; font-weight: 400; }
  .contact__title { font-size: 15px; margin-top: 16px; }
  .contact__lines { list-style: none; margin-top: 48px; font-size: 16px; line-height: 39px; }
</style>
</head>
<body>
<main class="sheet">

  <div class="wordmark logo-master">
    <span class="wordmark__square"></span>
    <span class="wordmark__text">Verdant<span class="wordmark__tag">Wares</span></span>
  </div>

  <section class="card-front" aria-label="Business card front">
    <div class="wordmark logo-front">
      <span class="wordmark__square"></span>
      <span class="wordmark__text">Verdant<span class="wordmark__tag">Wares</span></span>
    </div>
    <div class="card-front__band"></div>
  </section>

  <section class="card-back" aria-label="Business card back">
    <div class="wordmark logo-back">
      <span class="wordmark__square"></span>
      <span class="wordmark__text">Verdant<span class="wordmark__tag">Wares</span></span>
    </div>
    <div class="card-back__band"></div>
    <div class="contact">
      <p class="contact__name">Your Name</p>
      <p class="contact__title">Job Title</p>
      <ul class="contact__lines">
        <li>p (555) 555-5555</li>
        <li>f (555) 555-5555</li>
        <li>yourname@verdantwares.com</li>
      </ul>
    </div>
  </section>

</main>
</body>
</html>
```